Extend Medium Rectangle into Halfpage and Billboard Ad Format

We have a few variations of our Medium Rectangle (300x250) that we use to build scalable online ads for local advertisers based on their images and logos which in most of the cases are very basic but still should deliver decent results in terms of overall banner look.

Based on those variations we would like to have each a Halfpage and Billboard variation to it that resembles the "look & feel" to feel like "out of one hand" and allows the local advertiser to recognize his ad across all formats.

Core of the Medium Rectangle is a carousel ad to swipe through the images and "more information" for the click-out to the landingpage. That might be great to replicate on the other banner formats but also could be done differently.

Attached the examples we have for one local customer to build ads from. Very limited but realistic.

```html
<!DOCTYPE html>
<html lang="de">
<head>
<meta charset="utf-8">
<title>Gasthof Eiche – Anzeigenformate</title>
<link rel="stylesheet" href="https://fonts.googleapis.com/css2?family=Saira:wght@400;500&display=swap">
<style>
  :root {
    --stage: #2f2b2b;
    --red-light: #c00a0a;
    --red: #a80000;
    --red-dark: #6e0000;
    --white: #ffffff;
    --button-text: #b30000;
    --photo-house: linear-gradient(160deg, #dfe6ea 0%, #c9b98a 45%, #7c6a4a 75%, #5a5a50 100%);
    --photo-dish: linear-gradient(140deg, #e8ddd0 0%, #b9743a 40%, #7a3a1c 70%, #d9c060 100%);
    --photo-room: linear-gradient(120deg, #6b4a2c 0%, #d9c7a0 35%, #8e2020 60%, #5b3a24 100%);
  }
  * { margin: 0; padding: 0; box-sizing: border-box; }
  html, body { width: 1200px; height: 685px; overflow: hidden; }
  body { background: var(--stage); position: relative; font-family: "Saira", sans-serif; }

  .ad { position: absolute; overflow: hidden; }
  .photo { position: absolute; inset: 0; }
  .photo--house { background: var(--photo-house); }
  .photo--dish { background: var(--photo-dish); }
  .photo--room { background: var(--photo-room); }
  .panel-edge { position: absolute; inset: 0; background: var(--white); }
  .panel { position: absolute; inset: 0;
    background: radial-gradient(ellipse at 30% 20%, var(--red-light) 0%, var(--red) 45%, var(--red-dark) 100%); }

  .brand { position: absolute; color: var(--white); font-weight: 400; font-size: 23px; letter-spacing: 0.5px; line-height: 1; }
  .headline { position: absolute; color: var(--white); font-weight: 500; font-size: 15px; line-height: 19px; }
  .cta { position: absolute; width: 119px; height: 30px; background: var(--white); color: var(--button-text);
    font-size: 9.5px; font-weight: 500; letter-spacing: 0.4px; display: flex; align-items: center; justify-content: center; }
  .dots { position: absolute; display: flex; gap: 4.6px; }
  .dot { width: 8px; height: 8px; border-radius: 50%; border: 1px solid var(--white); }
  .dot--active { background: var(--white); }

  /* Billboard */
  .billboard { left: 35px; width: 505px; height: 158px; }
  .billboard .photo { right: 200px; }
  .billboard .panel-edge { clip-path: polygon(250px 0, 100% 0, 100% 100%, 200px 100%); }
  .billboard .panel { clip-path: polygon(258px 0, 100% 0, 100% 100%, 208px 100%); }
  .billboard .brand { left: 281px; top: 29px; }
  .billboard .headline { left: 266px; top: 60px; width: 230px; text-align: center; }
  .billboard .cta { left: 254px; top: 111px; }
  .billboard .dots { left: 452px; top: 130px; }

  /* Halfpage */
  .halfpage { top: 165px; width: 189px; height: 379px; }
  .halfpage .photo { top: 170px; }
  .halfpage .panel-edge { clip-path: polygon(0 0, 100% 0, 100% 222px, 0 181px); }
  .halfpage .panel { clip-path: polygon(0 0, 100% 0, 100% 213px, 0 177px); }
  .halfpage .brand { left: 0; width: 100%; text-align: center; top: 31px; }
  .halfpage .headline { left: 0; width: 100%; text-align: center; top: 63px; }
  .halfpage .cta { left: 36px; top: 134px; }
  .halfpage .dots { left: 79px; top: 350px; }
</style>
</head>
<body>

  <section class="ad billboard" style="top:102px">
    <div class="photo photo--house" role="img" aria-label="Außenansicht des Gasthofs"></div>
    <div class="panel-edge"></div><div class="panel"></div>
    <div class="brand">EICHE</div>
    <p class="headline">Neueröffnung Gasthof<br>Eiche in Tannbach!</p>
    <div class="cta">MEHR ERFAHREN</div>
    <div class="dots"><span class="dot dot--active"></span><span class="dot"></span><span class="dot"></span></div>
  </section>

  <section class="ad billboard" style="top:276px">
    <div class="photo photo--dish" role="img" aria-label="Angerichtetes Gericht mit Kräutern"></div>
    <div class="panel-edge"></div><div class="panel"></div>
    <div class="brand">EICHE</div>
    <p class="headline">Neueröffnung Gasthof<br>Eiche in Tannbach!</p>
    <div class="cta">MEHR ERFAHREN</div>
    <div class="dots"><span class="dot"></span><span class="dot dot--active"></span><span class="dot"></span></div>
  </section>

  <section class="ad billboard" style="top:448px">
    <div class="photo photo--room" role="img" aria-label="Gedeckter Gastraum"></div>
    <div class="panel-edge"></div><div class="panel"></div>
    <div class="brand">EICHE</div>
    <p class="headline">Neueröffnung Gasthof<br>Eiche in Tannbach!</p>
    <div class="cta">MEHR ERFAHREN</div>
    <div class="dots"><span class="dot"></span><span class="dot"></span><span class="dot dot--active"></span></div>
  </section>

  <section class="ad halfpage" style="left:567px">
    <div class="photo photo--house" role="img" aria-label="Außenansicht des Gasthofs"></div>
    <div class="panel-edge"></div><div class="panel"></div>
    <div class="brand">EICHE</div>
    <p class="headline">Neueröffnung<br>Gasthof Eiche in<br>Tannbach!</p>
    <div class="cta">MEHR ERFAHREN</div>
    <div class="dots"><span class="dot dot--active"></span><span class="dot"></span><span class="dot"></span></div>
  </section>

  <section class="ad halfpage" style="left:770px">
    <div class="photo photo--dish" role="img" aria-label="Angerichtetes Gericht mit Kräutern"></div>
    <div class="panel-edge"></div><div class="panel"></div>
    <div class="brand">EICHE</div>
    <p class="headline">Neueröffnung<br>Gasthof Eiche in<br>Tannbach!</p>
    <div class="cta">MEHR ERFAHREN</div>
    <div class="dots"><span class="dot"></span><span class="dot dot--active"></span><span class="dot"></span></div>
  </section>

  <section class="ad halfpage" style="left:973px">
    <div class="photo photo--room" role="img" aria-label="Gedeckter Gastraum"></div>
    <div class="panel-edge"></div><div class="panel"></div>
    <div class="brand">EICHE</div>
    <p class="headline">Neueröffnung<br>Gasthof Eiche in<br>Tannbach!</p>
    <div class="cta">MEHR ERFAHREN</div>
    <div class="dots"><span class="dot"></span><span class="dot"></span><span class="dot dot--active"></span></div>
  </section>

</body>
</html>
```